International Digitally Led Media Agency Requires a New Website

Brief Outline

• We are a growing business that has been established for approximately 2 years.

• Our current website did the job when Corvend Media began but it has not developed and progressed alongside the business (currently it does not represent nor portray the business appropriately).

• Corvend Media is a digitally led media agency that has numerous arms; 1) production based work (e.g. Paid Advertising, etc.) 2) consultancy and 3) Offline media (such as outdoor, TV, Radio)

• The business is globally focused and the website must reflect this.

• The new website is to portray the business more professionally with thought leadership at the forefront.

• The tone and voice of the website is to be clear, concise and straight talking.

• The website isn't to be a driver of new business (e.g. conversion based for enquiries) but is to support external new business activities. However, the website is to support the thought leadership marketing (specifically around content marketing - webinars, whitepapers, social, etc).

• We must be able to edit/upload/add content to the website very easily.

The current website is www.corvend-media.example

Current clients include
J&T - www.j&t.example
Folmary Trudesse - www.ft.example
KX Glow - www.kxglow.example
Lungwise UK - www.lungwise.example.uk
The Vantry Academy - www.vantry-academy.example.uk
Hale Retirement - www.haleretirement.example
Quillet Credit - www.quilletcredit.example.uk
DLMorvat - www.dl-morvat.example.uk
Perravine Lodging Collective - www.plc-lodging.example
Brindlewick - www.brindlewick.example
Varnique - www.varniqueit.example

Reason: We gave some delayed feedback to some desginers looking to enter the project and want to give them a chance to submit their designs.

Target Market(s)

Key decision makers within brands. Marketing Executives/Managers/Directors, Procurement Executives/Managers/Directors, Company Owners, CEO's /MD's

Industry/Entity Type

Business

Coding

Coded - Design and coding required

Number of Pages Required

5+ page

Font styles to use
Sans Serif

Requirements
Must have
• We definitely want video capability and the ability to add pages ourselves.
• We would like the layout to look something like
• HOME
•   
• 7dash3 > CASE STUDIES
• WHAT WE DO > CASE STUDIES
•  
• CONTACT
•  
• CLIENT LOGIN
Nice to have
• Social feeds

```html
<!DOCTYPE html>
<html lang="en">
<head>
<meta charset="utf-8">
<title>Corvend Media</title>
<link rel="stylesheet" href="https://fonts.googleapis.com/css2?family=Montserrat:wght@400;500;600;700&family=Open+Sans:wght@400;600&display=swap">
<style>
:root{
  --wine:#7b1a33;
  --wine-dark:#6a1229;
  --ink:#222;
  --text:#555;
  --muted:#888;
  --grey-bg:#e9e9e9;
  --footer-bg:#dcdcdc;
  --btn:#e3e3e3;
  --sky:#29a8e0;
  --navy:#0f3d99;
  --white:#fff;
}
*{margin:0;padding:0;box-sizing:border-box}
html,body{width:1200px;height:2278px;overflow:hidden;background:var(--white)}
body{position:relative;font-family:"Open Sans",Arial,sans-serif;color:var(--text)}
.abs{position:absolute}
.head-font{font-family:"Montserrat",Arial,sans-serif}

/* header */
.site-header{position:absolute;left:0;top:0;width:1200px;height:100px;background:var(--white);z-index:3}
.brand{position:absolute;left:130px;top:-8px;width:136px;height:136px;border-radius:50%;background:var(--white);z-index:4}
.brand-name{position:absolute;left:236px;top:36px;font-family:"Montserrat",Arial,sans-serif;font-weight:500;font-size:24px;letter-spacing:4px;color:#555;z-index:5}
.brand-dot{position:absolute;left:170px;top:32px;width:40px;height:40px;border:3px solid var(--wine);border-radius:50%;z-index:5}
.main-nav{position:absolute;top:43px;font-family:"Montserrat",Arial,sans-serif;font-size:15px;color:#666;text-transform:uppercase;z-index:5}
.main-nav span{position:absolute;white-space:nowrap}
.main-nav .active{color:#111;font-weight:600}
.client-login{position:absolute;left:930px;top:33px;width:130px;height:41px;background:var(--btn);font-family:"Montserrat",Arial,sans-serif;font-weight:600;font-size:13px;color:#222;text-align:center;line-height:41px;z-index:5}

/* hero */
.hero{position:absolute;left:0;top:100px;width:1200px;height:515px;background:linear-gradient(110deg,#5b4a3f 0%,#8a7260 30%,#c7a07a 55%,#a8641e 80%,#7a3d10 100%)}
.hero-title{position:absolute;left:0;width:1200px;text-align:center;color:var(--white);font-family:"Montserrat",Arial,sans-serif;font-weight:700;text-transform:uppercase;text-shadow:0 2px 6px rgba(0,0,0,.35)}
.hero-title.l1{top:292px;font-size:46px;letter-spacing:.5px}
.hero-title.l2{top:348px;font-size:31px}
.slider-dots span{position:absolute;top:572px;width:16px;height:16px;border-radius:50%;background:var(--white)}
.slider-dots span.off{background:transparent;border:2px solid var(--white)}

/* section titles */
.section-title{position:absolute;left:0;width:1200px;text-align:center;font-family:"Montserrat",Arial,sans-serif;font-size:31px;color:#111;text-transform:uppercase}

/* what we do */
.intro{position:absolute;left:160px;top:734px;width:880px;text-align:center;font-size:15px;line-height:27.5px;color:#666}

/* services */
.services{position:absolute;left:0;top:925px;width:1200px;height:375px;background:radial-gradient(circle at 30% 40%,#8c2440 0%,var(--wine) 55%,var(--wine-dark) 100%)}
.services-notch{position:absolute;left:576px;top:925px;width:0;height:0;border-left:24px solid transparent;border-right:24px solid transparent;border-top:24px solid var(--white)}
.service{position:absolute;width:260px;text-align:center;color:var(--white)}
.service h3{font-family:"Montserrat",Arial,sans-serif;font-weight:400;font-size:19px;margin-bottom:12px}
.service p{font-size:13px;line-height:20px;color:rgba(255,255,255,.7)}
.read-more-light{display:inline-block;margin-top:20px;font-family:"Montserrat",Arial,sans-serif;font-size:15px;color:var(--white);padding-bottom:4px;border-bottom:1px solid rgba(255,255,255,.7)}
.service-icon{position:absolute}

/* news */
.news{position:absolute;left:0;top:1300px;width:1200px;height:359px;background:var(--grey-bg)}
.news-photo{position:absolute;width:136px;height:136px;border-radius:50%;border:4px solid var(--white)}
.news-item{position:absolute;width:320px}
.news-item h4{font-family:"Open Sans",Arial,sans-serif;font-weight:400;font-size:19px;color:#444;margin-bottom:10px}
.news-item p{font-size:14px;line-height:25.5px;color:#999}
.read-more-dark{display:block;margin-top:6px;font-family:"Montserrat",Arial,sans-serif;font-size:14px;color:var(--wine)}

/* feeds */
.feed{position:absolute;top:1694px;height:299px;background:var(--white);border:1px solid #ccc;box-shadow:0 1px 3px rgba(0,0,0,.12);overflow:hidden}
.feed-head{height:46px;padding:0 24px;font-family:"Montserrat",Arial,sans-serif;font-size:19px;line-height:46px;border-bottom:1px solid #ddd}
.feed-chirp .feed-head{color:var(--sky);background:linear-gradient(#fff,#f1f1f1)}
.feed-post .feed-head{color:var(--white);background:var(--navy)}
.follow-badge{position:absolute;left:208px;top:17px;width:48px;height:15px;border-radius:2px;background:#dfe6ee;border:1px solid #b8c4d2}
.scrollbar{position:absolute;right:0;top:46px;width:12px;bottom:0;background:#f2f2f2}
.scrollbar i{position:absolute;left:2px;width:8px;background:#bdbdbd}
.post{position:absolute;left:24px;right:26px}
.avatar{position:absolute;left:0;top:0;width:36px;height:32px;background:linear-gradient(#9a8a78,#5e554d)}
.post-body{margin-left:44px}
.post-name{font-size:13px;color:#222}
.post-handle{font-size:11px;color:#888}
.post-text{font-size:10.5px;line-height:16px;color:#666;margin-top:8px}
.post-time{font-size:10.5px;margin-top:4px}
.feed-chirp .post-time{color:var(--sky)}
.feed-post .post-time{color:var(--navy);font-weight:600}
.feed-post .post-text{margin-top:0}

/* footer */
.site-footer{position:absolute;left:0;top:2080px;width:1200px;height:198px;background:var(--footer-bg);border-top:5px solid var(--wine)}
.footer-badge{position:absolute;left:560px;top:2046px;width:76px;height:76px;border-radius:50%;background:var(--white)}
.footer-nav{position:absolute;left:0;top:2140px;width:1200px;text-align:center;font-family:"Montserrat",Arial,sans-serif;font-size:15px;color:#333}
.footer-nav span{margin:0 19px}
.copyright{position:absolute;left:0;top:2175px;width:1200px;text-align:center;font-size:12px;color:#777}
.social span{position:absolute;top:2224px;width:18px;height:18px;border-radius:50%;background:#666}
</style>
</head>
<body>

<header class="site-header">
  <div class="brand"></div>
  <div class="brand-dot"></div>
  <div class="brand-name">CORVEND</div>
  <nav class="main-nav">
    <span class="active" style="left:500px">Home</span>
    <span style="left:580px">Our Work</span>
    <span style="left:697px">Who We Are</span>
    <span style="left:831px">Contact</span>
  </nav>
  <svg class="abs" style="left:488px;top:14px;z-index:5" width="70" height="76" viewBox="0 0 70 76">
    <path d="M20 6 A34 34 0 0 0 50 70" fill="none" stroke="var(--wine)" stroke-width="3"/>
  </svg>
  <div class="client-login">CLIENT LOGIN</div>
</header>
<svg class="abs" style="left:126px;top:-12px;z-index:4" width="144" height="144" viewBox="0 0 144 144">
  <path d="M30 20 A64 64 0 0 0 120 116" fill="none" stroke="var(--wine)" stroke-width="4"/>
</svg>

<section class="hero" role="img" aria-label="Hand using a tablet with glowing digital marketing icons">
</section>
<div class="hero-title l1">Got the feeling your digital</div>
<div class="hero-title l2">marketing just isn’t quite ‘there’?</div>
<div class="slider-dots">
  <span style="left:550px"></span><span style="left:577px"></span><span style="left:604px"></span><span class="off" style="left:631px"></span>
</div>

<svg class="abs" style="left:460px;top:652px" width="250" height="70" viewBox="0 0 250 70">
  <path d="M40 4 A34 34 0 0 0 8 40" fill="none" stroke="var(--wine)" stroke-width="3"/>
  <path d="M246 40 A34 34 0 0 1 200 68" fill="none" stroke="var(--wine)" stroke-width="3"/>
</svg>
<h2 class="section-title" style="top:673px">What we do</h2>
<p class="intro">We make your brand famous.&nbsp; To do this we optimise your website or any digital assets you have, so they can be found online, whether that is through search engines or social media.<br>Then we make sure your paid media is as efficient as possible. Your customer lives in the real world as well as online, so we have no restrictions. We work with our clients across organic search, paid search, display and social media as well as television, press and out of home advertising.</p>

<section class="services"></section>
<div class="services-notch"></div>

<svg class="service-icon" style="left:236px;top:986px" width="116" height="116" viewBox="0 0 116 116" fill="none" stroke="#fff" stroke-width="2.5">
  <path d="M58 6 A52 52 0 0 0 10 74" opacity=".9"/>
  <path d="M104 44 A52 52 0 0 1 44 108"/>
  <circle cx="44" cy="48" r="12"/><circle cx="44" cy="48" r="5"/>
  <circle cx="72" cy="70" r="12"/><circle cx="72" cy="70" r="5"/>
  <path d="M68 34 a20 20 0 0 1 16 12 M34 76 a20 20 0 0 0 18 10"/>
</svg>
<div class="service" style="left:169px;top:1112px"><h3>Production based work</h3><p>sociosqu ad litora torquent per conubia nostra per inceptos hymenaeos Proin nulla arcu nonummy luctu</p><span class="read-more-light">READ MORE</span></div>

<svg class="service-icon" style="left:548px;top:992px" width="116" height="116" viewBox="0 0 116 116" fill="none" stroke="#fff" stroke-width="2.5">
  <path d="M58 6 A52 52 0 0 0 10 74"/>
  <path d="M104 44 A52 52 0 0 1 44 108"/>
  <rect x="26" y="38" width="60" height="38" rx="4"/>
  <path d="M48 76 l6 12 l6 -12"/>
  <circle cx="44" cy="57" r="4"/><circle cx="56" cy="57" r="4"/><circle cx="68" cy="57" r="4"/>
</svg>
<div class="service" style="left:484px;top:1117px"><h3>Consultancy</h3><p>sociosqu ad litora torquent per conubia nostra per inceptos hymenaeos Proin nulla arcu nonummy luctu</p><span class="read-more-light">READ MORE</span></div>

<svg class="service-icon" style="left:852px;top:984px" width="116" height="116" viewBox="0 0 116 116" fill="none" stroke="#fff" stroke-width="2.5">
  <path d="M58 6 A52 52 0 0 0 10 74"/>
  <path d="M104 44 A52 52 0 0 1 44 108"/>
  <rect x="30" y="36" width="54" height="36" rx="2"/>
  <path d="M57 72 v8 M44 82 h26"/>
</svg>
<div class="service" style="left:784px;top:1110px"><h3>Offline Media</h3><p>sociosqu ad litora torquent per conubia nostra per inceptos hymenaeos Proin nulla arcu nonummy luctu</p><span class="read-more-light">READ MORE</span></div>

<section class="news"></section>
<svg class="abs" style="left:530px;top:1326px" width="160" height="78" viewBox="0 0 160 78">
  <path d="M38 4 A34 34 0 0 0 8 40" fill="none" stroke="var(--wine)" stroke-width="3"/>
  <path d="M152 40 A34 34 0 0 1 110 74" fill="none" stroke="var(--wine)" stroke-width="3"/>
</svg>
<h2 class="section-title" style="top:1346px">News</h2>

<div class="news-photo" role="img" aria-label="Two colleagues smiling at a laptop in a bright office" style="left:139px;top:1439px;background:linear-gradient(135deg,#d8d6d2,#8fa6c4 55%,#4e6e9a)"></div>
<div class="news-item" style="left:284px;top:1442px"><h4>Anterdum vel blandit sed nulla</h4><p>In ullamcorper est eget tempor cursus neque mi consectetuer mi a ultricies massa est sed nisl Class aptent taciti sociosqu ad litora</p><span class="read-more-dark">READ MORE</span></div>

<div class="news-photo" role="img" aria-label="Two people looking at a tablet together" style="left:596px;top:1439px;background:linear-gradient(135deg,#6d6f74,#a7a5a2 50%,#4c4b4d)"></div>
<div class="news-item" style="left:746px;top:1442px"><h4>Anterdum vel blandit sed nulla</h4><p>In ullamcorper est eget tempor cursus neque mi consectetuer mi a ultricies massa est sed nisl Class aptent taciti sociosqu ad litora</p><span class="read-more-dark">READ MORE</span></div>

<div class="feed feed-chirp" style="left:146px;width:436px">
  <div class="feed-head">Chirpline Feed</div>
  <span class="follow-badge"></span>
  <div class="scrollbar"><i style="top:46px;height:104px"></i></div>
  <div class="post" style="top:66px">
    <div class="avatar" role="img" aria-label="Profile photo"></div>
    <div class="post-body"><div class="post-name">Vestibulum ligula</div><div class="post-handle">@ inceptos hymenaeos</div></div>
    <div class="post-text">tricies eu volutpat non condimentum hendrerit augue Etiam eleifend metus vitae adipiscing semper mauris ipsum iaculis elit congue gravida elit mi egestas orci Curabitur pede ultricies sit amet porttitor m</div>
    <div class="post-time">2 days ago</div>
  </div>
  <div class="post" style="top:184px">
    <div class="avatar" role="img" aria-label="Profile photo"></div>
    <div class="post-body"><div class="post-name">Maecenas aliquet</div><div class="post-handle">@ inceptos hymenaeos</div></div>
    <div class="post-text">Curabitur metus ipsuaeos Proin nulla arcu nonummy luctus dictum eget fermentum et lorem Nunc porta convallis pede</div>
    <div class="post-time">2 days ago</div>
  </div>
</div>

<div class="feed feed-post" style="left:614px;width:448px">
  <div class="feed-head">Facepost Feed</div>
  <div class="scrollbar"><i style="top:46px;height:104px"></i></div>
  <div class="post" style="top:64px">
    <div class="avatar" role="img" aria-label="Profile photo"></div>
    <div class="post-body"><div class="post-name">Lorem ipsum dolor sit amet <span class="post-handle">@ iinterdum vel blandit sed</span></div>
    <div class="post-text">nulla In ullamcorper est eget tempor cursus neque mi consectetuer mi a ultricies massa est sed nisl Class aptent taciti sociosqu ad litora torquent per conubia nostra</div>
    <div class="post-time">2 days ago</div></div>
  </div>
  <div class="post" style="top:174px">
    <div class="avatar" role="img" aria-label="Profile photo"></div>
    <div class="post-body"><div class="post-name">Praesent elementum elit at tellus <span class="post-handle">@ iinterdum vel blandit</span></div>
    <div class="post-text">sed nulla In ullamcorper est eget tempor cursus neque mi consectetuer mi a ultricies massa est sed nisl Class aptent taciti sociosqu ad litora torquent per conubia nostra</div>
    <div class="post-time">5 days ago</div></div>
  </div>
</div>

<footer class="site-footer"></footer>
<div class="footer-badge"></div>
<svg class="abs" style="left:560px;top:2046px" width="76" height="76" viewBox="0 0 76 76">
  <path d="M60 62 A30 30 0 0 1 14 50" fill="none" stroke="var(--wine)" stroke-width="3"/>
  <circle cx="38" cy="34" r="11" fill="none" stroke="#666" stroke-width="2"/>
</svg>
<nav class="footer-nav"><span>HOME</span><span>OUR WORK</span><span>WHO WE ARE</span><span>BLOGS</span><span>NEWS</span><span>CONTACT</span></nav>
<div class="copyright">© 2016 Company Name&nbsp; All right reserved&nbsp; Term of Use</div>
<div class="social">
  <span style="left:504px"></span><span style="left:548px"></span><span style="left:595px"></span><span style="left:640px"></span><span style="left:685px"></span>
</div>

</body>
</html>
```